Single Page Digital Brochure

We are a Sydney based finance company. We lend money to developers. Please see attached example of what we are looking to have produced. We just need a design which can be posted on LINKEDIN

Target Market(s)

Property Developers who are borrowing money

Industry/Entity Type

Finance

Requirements
Must have
• Australian relevant imagery.

TEXT TO INCLUDE:

New Offering from Ferngate Lending
Nice to have
• Design and colour scheme based around our logo (attached)

Please include the same text as the attachment

Please make the design based loosely on the attachment. But do not copy the attachement
Should not have
• Remove Text: 'Settle in under four days'

```html
<!DOCTYPE html>
<html lang="en">
<head>
<meta charset="utf-8">
<title>Ferngate Lending – New Offering</title>
<link href="https://fonts.googleapis.com/css2?family=Montserrat:wght@500;600;700;800&display=swap" rel="stylesheet">
<style>
  :root {
    --page: #ffffff;
    --forest: #27483a;
    --white: #ffffff;
    --sky-top: #3a4560;
    --sky-warm: #7a5566;
    --harbour: #3a3f55;
    --shade: rgba(20, 24, 40, 0.35);
  }
  * { margin: 0; padding: 0; box-sizing: border-box; }
  html, body {
    width: 1200px; height: 1200px; overflow: hidden;
    background: var(--page);
    font-family: "Montserrat", Arial, sans-serif;
    color: var(--white);
  }
  .banner {
    position: absolute; left: 93px; top: 339px;
    width: 1021px; height: 529px;
  }
  .hero {
    position: relative; width: 100%; height: 407px; overflow: hidden;
  }
  .hero-photo {
    position: absolute; inset: 0;
    background:
      linear-gradient(180deg, var(--sky-top) 0%, var(--sky-warm) 30%, #4d4a5e 55%, var(--harbour) 100%);
  }
  .hero-photo::after {
    content: ""; position: absolute; inset: 0;
    background: linear-gradient(90deg, rgba(120,80,80,0.25) 0%, transparent 45%, var(--shade) 100%);
  }
  .headline {
    position: absolute; left: 68px; top: 44px;
    font-weight: 800; font-size: 62px; line-height: 69px;
    letter-spacing: 0.5px; text-transform: uppercase;
  }
  .deal-card {
    position: absolute; left: 581px; top: 51px;
    width: 352px; height: 318px;
  }
  .deal-card svg { position: absolute; inset: 0; }
  .deal-content { position: absolute; left: 38px; top: 33px; width: 290px; }
  .deal-title {
    font-weight: 700; font-size: 21px; line-height: 29px; text-transform: uppercase;
  }
  .deal-rule {
    width: 264px; height: 1px; background: var(--white); margin: 12px 0 17px;
  }
  .deal-terms { list-style: none; font-size: 12.5px; font-weight: 500; }
  .deal-terms li { line-height: 24px; white-space: nowrap; }
  .deal-terms b { font-weight: 700; }
  .contact-band {
    position: relative; height: 122px; background: var(--forest);
  }
  .contact-lines {
    position: absolute; left: 68px; top: 26px;
    font-size: 20px; font-weight: 500; letter-spacing: 0.3px;
  }
  .contact-line { display: flex; align-items: center; height: 38px; }
  .contact-line svg { margin: 0 12px 0 10px; }
  .band-divider {
    position: absolute; left: 635px; top: 22px; height: 78px;
    border-left: 1.5px dashed var(--white);
  }
  .brand {
    position: absolute; left: 660px; right: 0; top: 0; bottom: 0;
    display: flex; align-items: center; justify-content: center; gap: 12px;
  }
  .brand-dot { width: 22px; height: 22px; border-radius: 50%; background: var(--white); }
  .brand-name { font-size: 22px; font-weight: 600; letter-spacing: 1px; text-transform: uppercase; }
</style>
</head>
<body>
  <section class="banner">
    <div class="hero">
      <div class="hero-photo" role="img" aria-label="Sydney Harbour at dusk with the Opera House and city skyline"></div>
      <h1 class="headline">New<br>Offering<br>From<br>Ferngate<br>Lending</h1>
      <div class="deal-card">
        <svg width="352" height="318" viewBox="0 0 352 318" aria-hidden="true">
          <path d="M1 1 H351 V283 L317 317 H1 Z" fill="none" stroke="#ffffff" stroke-width="1.5"/>
        </svg>
        <div class="deal-content">
          <h2 class="deal-title">We did<br>just last week</h2>
          <div class="deal-rule"></div>
          <ul class="deal-terms">
            <li><b>Loan Amount:</b> $750,000</li>
            <li><b>Rate:</b> 7.79%</li>
            <li><b>Term:</b> 12months</li>
            <li><b>LVR:</b> 60%</li>
            <li><b>Repayments:</b> Capitalized</li>
            <li><b>Security:</b> 2x Sydney Residential Properties</li>
            <li><b>Purpose:</b> Business Working Capital</li>
          </ul>
        </div>
      </div>
    </div>
    <footer class="contact-band">
      <div class="contact-lines">
        <div class="contact-line">CALL LIAM TODAY ON -
          <svg width="26" height="26" viewBox="0 0 26 26" aria-hidden="true">
            <circle cx="13" cy="13" r="12" fill="none" stroke="#fff" stroke-width="1.5"/>
            <path d="M9 7.5 l2 -0.5 1.5 3.5 -1.5 1.2 c0.8 1.8 2 3 3.8 3.8 l1.2 -1.5 3.5 1.5 -0.5 2 c-5 0.5 -10.5 -5 -10 -10z" fill="none" stroke="#fff" stroke-width="1.3" stroke-linejoin="round"/>
          </svg>0400 318 562 or</div>
        <div class="contact-line">EMAIL -
          <svg width="26" height="26" viewBox="0 0 26 26" aria-hidden="true">
            <circle cx="13" cy="13" r="12" fill="none" stroke="#fff" stroke-width="1.5"/>
            <rect x="7" y="9" width="12" height="8.5" fill="none" stroke="#fff" stroke-width="1.2"/>
            <path d="M7 9 l6 5 6 -5 M7 17.5 l4.5 -4 M19 17.5 l-4.5 -4" fill="none" stroke="#fff" stroke-width="1.1"/>
          </svg>&nbsp;liam@ferngatelending.com</div>
      </div>
      <div class="band-divider"></div>
      <div class="brand">
        <span class="brand-dot"></span>
        <span class="brand-name">Ferngate Lending</span>
      </div>
    </footer>
  </section>
</body>
</html>
```